Zirkus Design (Hintergrund)
Zielgruppe
Familien, Eltern, Kinder (Jugendliche), LehrerInnen / Pädagogen, päd. Einrichtungen, Firmen
kreativ, künstlerisch, welt offen, international, sozial, engagiert, sportlich
Aufgabenstellung
Das Layout soll multifunktional sein, das heist in seinen Grundzügen oder leicht abgewandelt soll es für Postkarten, Flyer (DIN A 4 3 fach geknickt) und evtl. Plakate (als Hintergrund) Verwendung finden.
Und es soll für verschiedene Projekte / Veranstaltungen wiederverwendet werden, da ich nicht das Budget habe jedesmal ein neues Layout machen zu lassen.

```html
<!DOCTYPE html>
<html lang="de">
<head>
<meta charset="utf-8">
<title>Manege Lumen – Hintergrund</title>
<link href="https://fonts.googleapis.com/css2?family=Gochi+Hand&display=swap" rel="stylesheet">
<style>
  :root {
    --backdrop: #ffffff;
    --paper-light: #fbf5e6;
    --paper-warm: #f8e7bf;
    --circus-red: #c44133;
    --meadow-green: #93c155;
    --ring-white: #fdf8ee;
  }
  * { margin: 0; padding: 0; box-sizing: border-box; }
  html, body {
    width: 1200px;
    height: 900px;
    overflow: hidden;
    background: var(--backdrop);
  }
  .sheet {
    position: absolute;
    left: 319px;
    top: 43px;
    width: 562px;
    height: 795px;
    overflow: hidden;
    background: var(--paper-light);
  }
  .sheet-art {
    position: absolute;
    inset: 0;
    width: 100%;
    height: 100%;
    display: block;
  }
  .brand {
    position: absolute;
    right: 18px;
    top: 100px;
    text-align: right;
    font-family: "Gochi Hand", cursive;
    font-weight: 400;
  }
  .brand-name {
    display: flex;
    align-items: center;
    justify-content: flex-end;
    gap: 8px;
    font-size: 38px;
    line-height: 1;
    color: var(--circus-red);
  }
  .brand-dot {
    width: 12px;
    height: 12px;
    border-radius: 50%;
    border: 2px solid var(--circus-red);
  }
  .brand-person {
    margin-top: 4px;
    font-size: 15px;
    line-height: 1;
    color: var(--meadow-green);
  }
</style>
</head>
<body>
  <main class="sheet">
    <svg class="sheet-art" viewBox="0 0 480 678" preserveAspectRatio="none" aria-hidden="false">
      <defs>
        <radialGradient id="sunburst-glow" cx="0.55" cy="1" r="1.1">
          <stop offset="0" stop-color="var(--paper-light)"/>
          <stop offset="0.6" stop-color="var(--paper-warm)"/>
          <stop offset="1" stop-color="var(--paper-light)"/>
        </radialGradient>
        <linearGradient id="tent-tone" x1="0" y1="0" x2="0" y2="1">
          <stop offset="0" stop-color="#dbe9bf"/>
          <stop offset="1" stop-color="#b9d68a"/>
        </linearGradient>
      </defs>

      <rect class="sunburst-area" role="img" aria-label="Sonnenstrahlen in Creme- und Hellgelbtönen, die von unten über die Seite fächern" x="0" y="0" width="480" height="678" fill="url(#sunburst-glow)"/>

      <rect class="top-band" x="0" y="24" width="480" height="21" fill="var(--circus-red)"/>
      <circle class="band-bubble" cx="19" cy="36" r="6" fill="none" stroke="var(--ring-white)" stroke-width="2"/>
      <circle class="band-bubble" cx="47" cy="31" r="10" fill="none" stroke="var(--ring-white)" stroke-width="2"/>

      <ellipse class="ring ring-green" cx="412" cy="393" rx="74" ry="91" fill="none" stroke="var(--meadow-green)" stroke-width="13"/>
      <ellipse class="ring ring-red" cx="276" cy="498" rx="52" ry="52" fill="none" stroke="var(--circus-red)" stroke-width="14"/>

      <rect class="tent-area" role="img" aria-label="Skizzierte grüne Zirkuszelt-Zeichnung mit Fahne und zwei Seifenblasen" x="2" y="518" width="178" height="138" rx="14" fill="url(#tent-tone)" opacity="0.75"/>

      <path class="ground-band" d="M0 650 Q120 644 240 649 T480 646 L480 678 L0 678 Z" fill="var(--meadow-green)"/>
      <path class="ground-line" d="M20 654 Q200 650 400 651" fill="none" stroke="var(--ring-white)" stroke-width="1.5"/>
    </svg>

    <div class="brand">
      <div class="brand-name"><span class="brand-dot"></span>Manege Lumen</div>
      <div class="brand-person">Jonas Wedeking</div>
    </div>
  </main>
</body>
</html>
```